Corporate Design für aufstrebende Immobilienmaklerin
Herr Lanke ist auf alle Wünsche eingegangen und hat meine Erwartungen an den Ablauf des Projektes in vielerlei Hinsicht übertroffen. Auch als es von meiner Seite Verzögerung gab, war er sehr verständnisvoll und hat gewartet, bis alles soweit war. Würde immer wieder mit ihm arbeiten.
Zielgruppe
Ich bin eine junge Immobilienmaklerin, die sich neu am Markt etablieren möchte.
Mein Service für Kunden umfasst das folgende Programm:
Wertermittlung
Marktanalyse
Energieausweis
Vermarktung
z.T. Home Staging
Vorbereitung Kaufverträge
Begleitung zum Notar...
Zielgruppe: Immobilienbesitzer, Käufer, Verkäufer, alle die gerne einen Mehrwert rund um die Immobilie haben möchten
Aufgabenstellung
Ich suche ein Design für meine Geschäftsunterlagen. Der Betrachter soll ein gutes Gefühl bekommen. Es soll seriös, edel und dynamisch wirken. Aber vor allem auch vertrauensvoll und kompetent.
Das Logo sollte unverwechselbar, einfach und einprägsam sein. Ich könnte mir sehr gut einen Schlüssel vorstellen, da es ja am Ende des gesamten Prozesses stets um eine Schlüsselübergabe geht. Aber da bin ich auch für alles andere offen.
Es wäre schön, wenn das Design in 'Wohlfühlfarben' gehalten ist, nicht so knallig, eher elegant.

```html
<!DOCTYPE html>
<html lang="de">
<head>
<meta charset="utf-8">
<title>Wendt Immobilien – Visitenkarte</title>
<link rel="stylesheet" href="https://fonts.googleapis.com/css2?family=Quicksand:wght@400;700&display=swap">
<style>
  :root {
    --page: #eceae7;
    --coral: #e8604c;
    --greige: #bdb4aa;
    --band: #e9e6e2;
    --text-grey: #a09a94;
    --card-white: #ffffff;
    --dark-1: #7a7a7a;
    --dark-2: #4b4b4b;
    --dark-3: #383838;
    --logo-light: #f3f3f3;
  }
  * { box-sizing: border-box; margin: 0; padding: 0; }
  html, body { width: 1200px; height: 1200px; overflow: hidden; }
  body {
    background: var(--page);
    font-family: "Quicksand", "Helvetica Neue", Arial, sans-serif;
    display: flex; flex-direction: column; align-items: center; justify-content: center;
    gap: 60px;
  }
  .card {
    position: relative; width: 800px; height: 518px; overflow: hidden;
    box-shadow: 0 6px 18px rgba(0,0,0,.12);
  }
  .card-stripes { position: absolute; left: 0; right: 0; bottom: 0; }
  .stripe-greige { height: 16px; background: var(--greige); }
  .stripe-coral { height: 12px; background: var(--coral); }

  /* front */
  .card-front {
    background: radial-gradient(ellipse at 40% 45%, var(--dark-1) 0%, var(--dark-2) 60%, var(--dark-3) 100%);
  }
  .portrait {
    position: absolute; left: 110px; bottom: 28px; width: 360px; height: 420px;
    background: linear-gradient(180deg, #9c948c 0%, #b09a84 35%, #22407a 65%, #1c3a72 100%);
    border-radius: 160px 160px 0 0;
  }
  .front-logo {
    position: absolute; left: 470px; top: 170px;
    display: flex; flex-direction: column; color: var(--logo-light);
  }
  .front-logo .logo-word { font-size: 62px; letter-spacing: 6px; line-height: 1; display: flex; align-items: center; gap: 14px; }
  .front-logo .logo-mark { width: 18px; height: 18px; background: var(--logo-light); }
  .front-logo .logo-sub { font-size: 19px; letter-spacing: 9px; margin: 6px 0 0 34px; }
  .website {
    position: absolute; right: 40px; bottom: 48px;
    color: #d8d8d8; font-size: 19px; letter-spacing: 1px;
  }

  /* back */
  .card-back { background: var(--card-white); }
  .identity { position: absolute; left: 56px; top: 262px; }
  .name { color: var(--coral); font-size: 30px; font-weight: 400; letter-spacing: 1px; }
  .name strong { font-weight: 700; }
  .role { color: var(--text-grey); font-size: 18px; margin-top: 4px; }
  .contact-band {
    position: absolute; left: 0; right: 0; bottom: 12px; height: 170px; background: var(--band);
  }
  .contact-list {
    position: absolute; left: 56px; top: 58px;
    color: var(--text-grey); font-size: 18px; line-height: 26px; list-style: none;
  }
  .address {
    position: absolute; left: 300px; top: 6px;
    color: var(--text-grey); font-size: 18px; line-height: 26px; font-style: normal;
  }
  .back-logo {
    position: absolute; right: 40px; top: 2px; color: var(--coral);
    display: flex; flex-direction: column; align-items: flex-start;
  }
  .back-logo .logo-word { font-size: 42px; letter-spacing: 4px; line-height: 1; display: flex; align-items: center; gap: 10px; }
  .back-logo .logo-mark { width: 13px; height: 13px; background: var(--coral); }
  .back-logo .logo-sub { font-size: 14px; letter-spacing: 6px; margin: 4px 0 0 24px; }
  .card-back .stripe-coral { height: 12px; }
</style>
</head>
<body>
  <section class="card card-front">
    <div class="portrait" role="img" aria-label="Porträtfoto der Maklerin in blauem Poloshirt vor grauem Hintergrund"></div>
    <div class="front-logo">
      <span class="logo-word"><span class="logo-mark"></span>WENDT</span>
      <span class="logo-sub">IMMOBILIEN</span>
    </div>
    <p class="website">www.wendt-immobilien.de</p>
    <div class="card-stripes">
      <div class="stripe-greige"></div>
      <div class="stripe-coral"></div>
    </div>
  </section>

  <section class="card card-back">
    <div class="identity">
      <h1 class="name">Carola <strong>Wendt</strong></h1>
      <p class="role">Fachmaklerin der Immobilienwirtschaft VIMD</p>
    </div>
    <div class="contact-band">
      <ul class="contact-list">
        <li>Mobil: 0151-24 63 90 7</li>
        <li>info@wendt-immobilien.de</li>
      </ul>
      <address class="address">Lindenweg 14<br>59410 Seewalde</address>
      <div class="back-logo">
        <span class="logo-word"><span class="logo-mark"></span>WENDT</span>
        <span class="logo-sub">IMMOBILIEN</span>
      </div>
    </div>
    <div class="card-stripes">
      <div class="stripe-coral"></div>
    </div>
  </section>
</body>
</html>
```